Heron Freightlines needs Bussiness cards!

Our new trucking company needs business cards!
We need the same design with two different names and emails, everything else it's the same.
I have included our original logo so we can use it for the design.
Note: the logo to be used is the o e with the buffalo on the right side, next to the letters H and F.

Target Market(s)

Trucking, refrigerated transportation, freight

Industry/Entity Type

Business

Contact Information for Business Card

Card #1:
Marcus Tellwright
marcustellwright@heronfreightlines.example
1-844-555-0193
(612)555-0178
3817 W. Tarrow Ave.
Alder Bend, OR 78599
www.heronfreightlines.example

Card#2:
Orla Brennick
orla@heronfreightlines.example
1-844-555-0193
(612)555-0178
3817 W. Tarrow Ave.
Alder Bend, OR 78599
www.heronfreightlines.example

Font styles to use
Sans Serif

Colors
0655a3
ec1f27
ffffff

Requirements
Must have
• our logo
Nice to have
• roads on background,

```html
<!DOCTYPE html>
<html lang="en">
<head>
<meta charset="utf-8">
<title>Heron Freightlines – Business Card</title>
<link href="https://fonts.googleapis.com/css2?family=Montserrat:wght@400;500;700;800&display=swap" rel="stylesheet">
<style>
  :root {
    --brand-red: #b5151d;
    --brand-navy: #0f3c6e;
    --card-white: #ffffff;
    --backdrop: #2b2b2d;
  }
  * { box-sizing: border-box; margin: 0; padding: 0; }
  html, body {
    width: 1200px; height: 900px; overflow: hidden;
    background: var(--backdrop);
    font-family: "Montserrat", Arial, sans-serif;
  }
  .canvas { position: relative; width: 1200px; height: 900px; }
  .card {
    position: absolute; left: 268px; width: 664px; height: 380px;
    border-radius: 26px; overflow: hidden;
  }
  .card-back { top: 45px; background: var(--brand-red); }
  .card-front { top: 475px; background: var(--card-white); }

  .back-mark {
    position: absolute; right: 70px; top: 96px;
    display: flex; align-items: center; gap: 14px;
  }
  .back-mark .dot { width: 18px; height: 18px; border-radius: 50%; background: var(--card-white); }
  .back-mark .wordmark { color: var(--card-white); font-weight: 700; font-size: 34px; }
  .back-url {
    position: absolute; left: 160px; top: 252px;
    color: var(--card-white); font-size: 22px; font-weight: 400; letter-spacing: 0.5px;
  }

  .front-logo {
    position: absolute; right: 44px; top: 48px;
    display: flex; align-items: center; gap: 12px;
  }
  .front-logo .dot { width: 18px; height: 18px; border-radius: 50%; background: var(--brand-navy); }
  .front-logo .wordmark { color: var(--brand-navy); font-weight: 800; font-size: 32px; }

  .side-band {
    position: absolute; left: 0; bottom: 0; width: 22px; height: 180px;
    background: var(--brand-navy); border-top-right-radius: 18px;
  }
  .contact { position: absolute; left: 58px; top: 196px; color: var(--brand-navy); }
  .contact .name {
    color: var(--brand-red); font-weight: 700; font-size: 24px; letter-spacing: 0.5px;
    margin-bottom: 8px; text-transform: uppercase;
  }
  .contact .line { font-size: 16px; line-height: 22px; font-weight: 500; }
  .contact .address { margin-bottom: 6px; }
  .contact .icon-line { display: flex; align-items: center; gap: 10px; }
  .contact svg { width: 14px; height: 14px; flex: none; }
</style>
</head>
<body>
<main class="canvas">
  <section class="card card-back" aria-label="Card back">
    <div class="back-mark">
      <span class="dot"></span>
      <span class="wordmark">Heron Freightlines</span>
    </div>
    <p class="back-url">www.heronfreightlines.example</p>
  </section>

  <section class="card card-front" aria-label="Card front">
    <div class="front-logo">
      <span class="dot"></span>
      <span class="wordmark">Heron Freightlines</span>
    </div>
    <div class="side-band"></div>
    <div class="contact">
      <p class="name">Marcus Tellwright</p>
      <div class="address">
        <p class="line">3817 W. Tarrow Ave.</p>
        <p class="line">Alder Bend, OR 78599</p>
      </div>
      <p class="line icon-line">
        <svg viewBox="0 0 24 24" aria-hidden="true"><path fill="#b5151d" d="M6.6 10.8a15 15 0 0 0 6.6 6.6l2.2-2.2c.3-.3.7-.4 1-.2 1.1.4 2.3.6 3.6.6.6 0 1 .4 1 1V20c0 .6-.4 1-1 1A17 17 0 0 1 3 4c0-.6.4-1 1-1h3.5c.6 0 1 .4 1 1 0 1.3.2 2.5.6 3.6.1.3 0 .7-.2 1z"/></svg>
        1-844-555-0193
      </p>
      <p class="line icon-line">
        <svg viewBox="0 0 24 24" aria-hidden="true"><rect x="6" y="2" width="12" height="20" rx="2" fill="none" stroke="#b5151d" stroke-width="2.4"/><circle cx="12" cy="18" r="1.3" fill="#b5151d"/></svg>
        (612)555-0178
      </p>
      <p class="line icon-line">
        <svg viewBox="0 0 24 24" aria-hidden="true"><circle cx="12" cy="12" r="9" fill="none" stroke="#b5151d" stroke-width="2"/><path d="M3 12h18M12 3c3 3 3 15 0 18M12 3c-3 3-3 15 0 18" fill="none" stroke="#b5151d" stroke-width="1.6"/></svg>
        www.heronfreightlines.example
      </p>
      <p class="line icon-line">
        <svg viewBox="0 0 24 24" aria-hidden="true"><rect x="2" y="5" width="20" height="14" rx="1.5" fill="none" stroke="#b5151d" stroke-width="2.2"/><path d="M3 6l9 7 9-7" fill="none" stroke="#b5151d" stroke-width="2"/></svg>
        marcustellwright@heronfreightlines.example
      </p>
    </div>
  </section>
</main>
</body>
</html>
```